Sudden Tides "Lantern Road" New Single Cover

Create cover artwork for the band Sudden Tides' new single "Lantern Road" being released early 2020. Style, font and graphics to be consistent with band's previous releases and overall brand identity. Visit www.suddentidesband.example and our Spotify page https://music.example.net/artist/7QzWpLx3RtVnKd8e2YbHcJ?si=MUrTgKa4PLe7skvWq2AmZd to view our previous releases and overall brand identity. Some examples attached as well. We are looking for someone to work with on future projects as well.

Lyrics are here: https://docs.example.org/document/d/3KTp9wrn_2ZQa8eXb4Lo_fimH7C5m83Jz4Pd70hrtVcA/edit

Music is here: https://audiostream.example.com/suddentides/lantern-road/s-pzkwa

Font styles to use
Sans Serif

Colors

Designer to choose colors to be used in the design.

Requirements
Must have
• Must be consistent with current brand identity and with prior album / single art.

```html
<!DOCTYPE html>
<html lang="en">
<head>
<meta charset="utf-8">
<title>Sudden Tides – Lantern Road</title>
<link rel="stylesheet" href="https://fonts.googleapis.com/css2?family=Questrial&display=swap">
<style>
  :root {
    --cover-pink: #ee0f7e;
    --title-white: #ffffff;
    --accent-navy: #06038d;
    --band-ink: #1a1240;
  }
  html, body {
    margin: 0;
    padding: 0;
    width: 1200px;
    height: 1200px;
    overflow: hidden;
    background: var(--cover-pink);
  }
  .cover {
    display: block;
    width: 1200px;
    height: 1200px;
  }
  .cover-background { fill: var(--cover-pink); }
  .gradient-stop--light { stop-color: var(--title-white); stop-opacity: 0.55; }
  .gradient-stop--navy { stop-color: var(--accent-navy); stop-opacity: 0.35; }
  .gradient-stop--pink { stop-color: var(--cover-pink); stop-opacity: 1; }
  .single-title {
    font-family: "Questrial", sans-serif;
    font-size: 280px;
    fill: var(--title-white);
  }
  .band-name {
    font-family: "Questrial", sans-serif;
    font-size: 54px;
    letter-spacing: 6px;
    fill: var(--band-ink);
  }
</style>
</head>
<body>
<svg class="cover" viewBox="0 0 1200 1200" xmlns="http://www.w3.org/2000/svg" role="img" aria-label="Sudden Tides – Lantern Road single cover">
  <defs>
    <linearGradient id="artwork-wash" x1="0" y1="0" x2="0" y2="1">
      <stop offset="0" class="gradient-stop--light"/>
      <stop offset="0.55" class="gradient-stop--navy"/>
      <stop offset="1" class="gradient-stop--pink"/>
    </linearGradient>
  </defs>

  <rect class="cover-background" x="0" y="0" width="1200" height="1200"/>

  <polygon class="artwork-area" points="120,0 1080,0 600,478" fill="url(#artwork-wash)"
           role="img" aria-label="Downward chevron artwork in white and navy stripes"/>

  <text class="single-title" x="74" y="840" textLength="1054" lengthAdjust="spacingAndGlyphs">LANTERN</text>
  <text class="single-title" x="74" y="1113" textLength="629" lengthAdjust="spacingAndGlyphs">ROAD</text>

  <text class="band-name" x="1130" y="1055" text-anchor="end">SUDDEN</text>
  <text class="band-name" x="1130" y="1113" text-anchor="end">TIDES</text>
</svg>
</body>
</html>
```